Local Flower Farm Needs Business Card Design

I need business cards designed for a flower farm based in Eudora, Kansas.
Business Info:
We are a local cut flower farm located in Eudora, Kansas, founded by Darla Whitcombe. What started as a passion for agriculture and search for more joy in daily life has blossomed into a small business dedicated to providing the community with beautiful, fresh, and sustainable flowers. We specialize in local, seasonal blooms, ensuring that every petal reflects the care and dedication we pour into our craft. Our mission is to deliver the highest quality flowers directly to our customers through local farmers markets and to florists who share our commitment to sustainability. Join us in celebrating the beauty of nature, one bloom at a time!
Contact Details:
Darla Whitcombe
Owner
Phone 913-555-0148
Facebook: Rosalind Pike Gardens
Instagram: @RosalindPikeGardens
Website: RosalindPikeGardens.example
Target Market(s)
Wholesale to Florists and Direct to Consumer via Farmers Market
Industry/Entity Type
Florist, Farm
Contact Information for Business Card
Name, Contact Info, Logo
Look and feel
Each slider illustrates characteristics of the customer's brand and the style your logo design should communicate.

```html
<!DOCTYPE html>
<html lang="en">
<head>
<meta charset="utf-8">
<title>Rosalind Pike Gardens – Business Card</title>
<link href="https://fonts.googleapis.com/css2?family=Cormorant+Garamond:wght@500&family=Montserrat:wght@400;700&display=swap" rel="stylesheet">
<style>
  :root {
    --backdrop: #1c1c1c;
    --teal-deep: #0c2628;
    --teal-mid: #17373a;
    --teal-light: #2e5154;
    --paper: #ffffff;
    --ink: #12292c;
  }
  * { margin: 0; padding: 0; box-sizing: border-box; }
  html, body { width: 1200px; height: 988px; overflow: hidden; background: var(--backdrop); }
  .canvas { position: relative; width: 1200px; height: 988px; }

  .card {
    position: absolute; left: 250px; width: 700px; height: 400px;
    border-radius: 26px; overflow: hidden;
  }
  .card--front { top: 64px;
    background: linear-gradient(135deg, var(--teal-light) 0%, var(--teal-mid) 30%, var(--teal-deep) 62%, var(--teal-deep) 100%);
  }
  .card--back { top: 524px; background: var(--paper); }

  .brand-seal {
    position: absolute; border-radius: 50%;
    display: flex; align-items: center; justify-content: center; text-align: center;
    font-family: "Cormorant Garamond", serif; font-weight: 500;
    letter-spacing: 0.12em; text-transform: uppercase; line-height: 1.25;
  }
  .card--front .brand-seal {
    left: 228px; top: 78px; width: 244px; height: 244px;
    border: 1.5px solid var(--paper); color: var(--paper); font-size: 27px;
  }
  .card--back .brand-seal {
    left: 30px; top: 26px; width: 150px; height: 150px;
    border: 1px solid var(--ink); color: var(--ink); font-size: 17px;
  }

  .identity { position: absolute; right: 42px; top: 52px; text-align: right; font-family: "Montserrat", sans-serif; color: var(--ink); }
  .identity__name { font-weight: 700; font-size: 27px; letter-spacing: 0.02em; text-transform: uppercase; }
  .identity__role { font-weight: 400; font-size: 15px; letter-spacing: 0.06em; text-transform: uppercase; margin-top: 2px; }
  .identity-rule { position: absolute; left: 200px; right: 90px; top: 122px; height: 1.5px; background: var(--ink); }
  .edge-tab { position: absolute; right: 0; top: 34px; width: 18px; height: 40px; background: var(--ink); border-radius: 4px 0 0 4px; }

  .contact-rule { position: absolute; left: 30px; width: 230px; top: 206px; height: 1.5px; background: var(--ink); }
  .contact-list { position: absolute; left: 30px; top: 218px; list-style: none; font-family: "Montserrat", sans-serif; color: var(--ink); font-size: 17px; }
  .contact-list li { display: flex; align-items: center; gap: 10px; height: 27px; }
  .contact-list svg { width: 14px; height: 14px; flex: none; }
  .contact-list .divider { height: 18px; }
  .contact-list .divider span { display: block; width: 12px; height: 1.5px; background: var(--ink); }
  .social-dot { width: 13px; height: 13px; border-radius: 50%; background: var(--ink); flex: none; }
</style>
</head>
<body>
<main class="canvas">
  <section class="card card--front">
    <div class="brand-seal">Rosalind<br>Pike<br>Gardens</div>
  </section>

  <section class="card card--back">
    <div class="edge-tab"></div>
    <div class="brand-seal">Rosalind<br>Pike<br>Gardens</div>
    <div class="identity">
      <div class="identity__name">Darla Whitcombe</div>
      <div class="identity__role">Owner</div>
    </div>
    <div class="identity-rule"></div>

    <div class="contact-rule"></div>
    <ul class="contact-list">
      <li>
        <svg viewBox="0 0 16 16" aria-hidden="true"><path fill="#12292c" d="M3.5 1.5l2.5 0 1 3.5-1.6 1.2c.8 1.7 2.1 3 3.8 3.8L10.4 8.4l3.5 1V12c0 1-.8 1.8-1.8 1.8C6.6 13.6 2.4 9.4 1.8 3.9 1.8 2.5 2.5 1.5 3.5 1.5z"/></svg>
        913-555-0148
      </li>
      <li>
        <svg viewBox="0 0 16 16" aria-hidden="true"><rect x="1" y="3" width="14" height="10" rx="1" fill="#12292c"/><path d="M1.5 3.8L8 9l6.5-5.2" stroke="#fff" stroke-width="1.2" fill="none"/></svg>
        info@RosalindPikeGardens.example
      </li>
      <li>
        <svg viewBox="0 0 16 16" aria-hidden="true"><g fill="none" stroke="#12292c" stroke-width="1.3"><circle cx="8" cy="8" r="6.5"/><ellipse cx="8" cy="8" rx="3" ry="6.5"/><path d="M1.5 8h13M2.5 4.8h11M2.5 11.2h11"/></g></svg>
        www.RosalindPikeGardens.example
      </li>
      <li class="divider"><span></span></li>
      <li><span class="social-dot"></span>Rosalind Pike Gardens</li>
      <li><span class="social-dot"></span>@RosalindPikeGardens</li>
    </ul>
  </section>
</main>
</body>
</html>
```